General Contractors need a new Crisp updated Card Design

We need a new business card design for our company of 25 years based in Toronto call Holvaster Building Inc. : Our goal is to be the leading commercial contractors in Toronto by providing exceptional value to our clients. We work very hard to deliver professional, quality, service in conjunction with consistent price competitiveness to all of our clients on every single project.

Target Market(s)

Design & Build Clients

Industry/Entity Type

Construction Company

Contact Information for Business Card

Address:
18 North Tamlin Glen Road, Unit 57, Marbrook Vale, ON, K7T 2R9
Office: 905-218-5937

Holvasters Logo
Employee Job Description
Employee Cell Phone #
Employee Email
www.holvaster-example.com

Colors

Designer to choose colors to be used in the design.

Requirements
Must have
• Quote Company Saying:
• "Professional. Quality. Service."
Nice to have
• New Crisp up to date look. simple & fresh ( Not to Busy)
Should not have
• NO BLUE PRINTS ON THE BUSINESS CARDS

```html
<!DOCTYPE html>
<html lang="en">
<head>
<meta charset="utf-8">
<title>Holvaster Building Inc. — Business Card</title>
<link rel="stylesheet" href="https://fonts.googleapis.com/css2?family=Alegreya+SC:ital,wght@0,400;1,400&family=EB+Garamond:wght@400;600;700&display=swap">
<style>
  :root {
    --brand-green: #1b915a;
    --brand-green-dark: #1d7a48;
    --band-mint: #b0e2bf;
    --band-rule: #2a9a5a;
    --slate-green: #3d6352;
    --tag-green: #2f6b4a;
    --ink: #1e2a24;
    --paper: #ffffff;
    --box-edge: #9fd8b4;
  }
  * { margin: 0; padding: 0; box-sizing: border-box; }
  html, body { width: 1119px; height: 1200px; overflow: hidden; background: var(--paper); }
  .card { position: relative; width: 1119px; height: 1200px; background: var(--paper); }

  .brand-mark {
    position: absolute; left: 0; right: 0;
    display: flex; align-items: center; justify-content: center; gap: 22px;
  }
  .brand-mark .mark-square { width: 112px; height: 112px; }
  .brand-mark .mark-name {
    font-family: "EB Garamond", serif; font-weight: 700;
    font-size: 50px; line-height: 1.02; letter-spacing: 1px; text-transform: uppercase;
  }
  .brand-mark--front { top: 6px; }
  .brand-mark--front .mark-square { background: var(--brand-green-dark); }
  .brand-mark--front .mark-name { color: var(--brand-green-dark); }

  .address {
    position: absolute; top: 172px; left: 0; right: 0; text-align: center;
    font-family: "Alegreya SC", serif; font-style: italic; color: var(--slate-green);
    line-height: 1.05;
  }
  .address .line-one { display: block; font-size: 44px; }
  .address .line-two { display: block; font-size: 38px; }

  .contact-band {
    position: absolute; top: 307px; left: 0; width: 1119px; height: 223px;
    background: var(--band-mint);
    border-top: 2px solid var(--band-rule); border-bottom: 2px solid var(--band-rule);
    text-align: center; font-family: "EB Garamond", serif; color: var(--ink);
  }
  .contact-band .job-title { position: absolute; top: 22px; left: 0; right: 0; font-size: 47px; }
  .contact-band .cell { position: absolute; top: 92px; left: 0; right: 0; font-size: 38px; }
  .contact-band .email { position: absolute; top: 156px; left: 0; right: 0; font-size: 38px; }

  .fold-line {
    position: absolute; top: 571px; left: 0; width: 1119px; height: 2px;
    background: repeating-linear-gradient(90deg, var(--ink) 0 20px, transparent 20px 33px);
  }

  .tagline {
    position: absolute; top: 612px; left: 0; right: 0; text-align: center;
    font-family: "Alegreya SC", serif; font-size: 52px; color: var(--tag-green);
    word-spacing: 0;
  }
  .tagline span { margin: 0 20px; }

  .brand-panel {
    position: absolute; left: 75px; top: 703px; width: 968px; height: 347px;
    background: var(--brand-green); border: 2px solid var(--box-edge);
  }
  .brand-mark--reverse { top: 825px; }
  .brand-mark--reverse .mark-square { border: 3px solid var(--paper); width: 116px; height: 116px; }
  .brand-mark--reverse .mark-name { color: var(--paper); }

  .office-phone {
    position: absolute; top: 1072px; left: 0; right: 0; text-align: center;
    font-family: "EB Garamond", serif; font-weight: 700; font-size: 49px; color: var(--tag-green);
  }
  .website {
    position: absolute; top: 1140px; left: 0; right: 0; text-align: center;
    font-family: "EB Garamond", serif; font-size: 41px; color: var(--ink);
  }
</style>
</head>
<body>
<main class="card">
  <div class="brand-mark brand-mark--front">
    <span class="mark-square"></span>
    <span class="mark-name">Holvaster<br>Building Inc.</span>
  </div>

  <p class="address">
    <span class="line-one">18 North Tamlin Glen Road,</span>
    <span class="line-two">Unit 57, Marbrook Vale, ON, K7T 2R9</span>
  </p>

  <section class="contact-band">
    <p class="job-title">Employee Job Description</p>
    <p class="cell">Cell# 905-000-0000</p>
    <p class="email">email@holvaster-example.com</p>
  </section>

  <div class="fold-line"></div>

  <p class="tagline"><span>Professional.</span><span>Quality.</span><span>Service.</span></p>

  <div class="brand-panel"></div>
  <div class="brand-mark brand-mark--reverse">
    <span class="mark-square"></span>
    <span class="mark-name">Holvaster<br>Building Inc.</span>
  </div>

  <p class="office-phone">905-218-5937</p>
  <p class="website">www.holvaster-example.com</p>
</main>
</body>
</html>
```